Compnay PowerPoint Tempalte Design

I am needing a good base design and slide designs for interior and exterior company presentations. The template will need to be on the company brand with proper coloring and fonts. Able to be creative with layout options with a good example attached.
website for reference: www.crewplorvane.com/

Target Market(s)

Professionals

Font styles to use
Other font styles liked:
• Helvetica

Requirements
Must have
• On Brand Colors, Clean, simple design

```html
<!DOCTYPE html>
<html lang="en">
<head>
<meta charset="utf-8">
<title>Crewplorvane Presentation Template</title>
<link href="https://fonts.googleapis.com/css2?family=Arimo:ital,wght@0,400;0,700;1,400&display=swap" rel="stylesheet">
<style>
:root{
  --page:#f3f3f3;
  --white:#ffffff;
  --ink:#1c1c1c;
  --forest:#1d4a3e;
  --teal:#3d8c7c;
  --ocean:#136590;
  --lime:#86bc2f;
  --mint:#33b882;
  --text:#555a5c;
  --star:#f08a1c;
  --line:#e3e5e6;
}
*{box-sizing:border-box;margin:0;padding:0}
html,body{width:1200px;height:4208px;overflow:hidden}
body{background:var(--page);font-family:"Arimo",Helvetica,Arial,sans-serif;color:var(--ink);position:relative}
.slide{position:absolute;left:51px;width:1098px;height:620px;background:var(--white);box-shadow:0 2px 8px rgba(0,0,0,.12);overflow:hidden}
.slide-cover{top:69px}
.slide-about{top:769px}
.slide-values{top:1461px}
.slide-team{top:2137px}
.slide-services{top:2834px}
.slide-thanks{top:3513px;background:var(--ocean)}
.abs{position:absolute}
.corner-mark{position:absolute;right:16px;bottom:14px;font-weight:700;font-size:15px;color:var(--forest)}
.heading{font-weight:700;color:var(--forest);text-align:center;font-size:42px;letter-spacing:.5px}
.rule{width:54px;height:3px;background:var(--forest);margin:12px auto 0}
.centered{left:0;right:0}
.photo{position:absolute}
.cover-name{left:106px;top:372px;font-size:60px;font-weight:700;color:var(--ink);letter-spacing:-1px}
.about-title{left:647px;top:100px;font-size:52px;font-weight:700;color:var(--forest)}
.about-rule{left:647px;top:162px;width:54px;height:3px;background:var(--forest)}
.about-copy{left:647px;top:185px;width:440px;font-size:11.2px;line-height:23px;color:var(--text)}
.about-copy p+p{margin-top:23px}
.value-label{position:absolute;width:200px;text-align:center}
.value-label h3{font-size:19px;font-weight:700;letter-spacing:.5px}
.value-label p{font-size:10.5px;line-height:18px;color:var(--text);margin-top:4px}
.hub-name{font-weight:700;font-size:24px;fill:var(--forest)}
.cards{position:absolute;left:28px;top:129px;display:flex;gap:31px}
.team-card{width:326px;height:398px;border:1px solid var(--line);box-shadow:0 1px 4px rgba(0,0,0,.06);padding:38px 26px 0}
.stars{display:flex;align-items:center;gap:6px;color:var(--star);font-size:15px}
.quote-mark{color:#8a8f91;font-weight:700;font-size:26px;line-height:14px;margin-right:4px}
.team-card blockquote{font-style:italic;font-size:12.3px;line-height:24.5px;color:var(--text);margin-top:20px;text-align:justify;height:230px}
.person{display:flex;align-items:center;gap:14px;margin-top:10px}
.avatar{width:80px;height:80px;border-radius:50%;background:linear-gradient(140deg,#c8b4a4,#6b5d55)}
.person h4{font-size:12.5px;line-height:22px;font-weight:700;color:#2a2a2a}
.service{width:326px;height:397px;display:flex;flex-direction:column}
.service .photo{position:static;height:312px}
.service h3{height:85px;display:flex;align-items:center;justify-content:center;color:var(--white);font-size:21px;font-weight:700;letter-spacing:.5px}
.thanks-title{top:315px;font-size:118px;font-weight:700;color:var(--white);text-align:center;letter-spacing:2px}
</style>
</head>
<body>

<section class="slide slide-cover">
  <svg class="abs" width="1098" height="620" viewBox="0 0 1098 620">
    <defs>
      <linearGradient id="crowdTone" x1="0" y1="0" x2="1" y2="1">
        <stop offset="0" stop-color="#cdd1d2"/>
        <stop offset=".5" stop-color="#6f6a66"/>
        <stop offset="1" stop-color="#3f4a56"/>
      </linearGradient>
      <linearGradient id="fadeTone" x1="0" y1="0" x2="1" y2="0">
        <stop offset="0" stop-color="#ffffff"/>
        <stop offset="1" stop-color="#eceeee"/>
      </linearGradient>
    </defs>
    <rect width="1098" height="620" fill="url(#fadeTone)"/>
    <polygon points="333,0 1098,0 1098,620 635,620" fill="url(#crowdTone)" role="img" aria-label="Photo of five smiling young team members standing arm in arm"/>
    <polygon points="333,0 358,0 455,190 440,205" fill="var(--ocean)"/>
    <line x1="300" y1="0" x2="345" y2="55" stroke="var(--teal)" stroke-width="2"/>
    <line x1="590" y1="530" x2="640" y2="620" stroke="#fff" stroke-width="3"/>
    <polygon points="0,538 25,580 575,580 597,620 0,620" fill="var(--forest)"/>
  </svg>
  <div class="abs cover-name">Crewplorvane</div>
</section>

<section class="slide slide-about">
  <div class="photo" style="left:49px;top:82px;width:269px;height:338px;background:linear-gradient(160deg,#6d5a46,#2f2620)" role="img" aria-label="Photo of a woman smiling with a coffee cup in a café"></div>
  <div class="photo" style="left:348px;top:113px;width:228px;height:225px;border:4px solid #fff;box-shadow:0 1px 5px rgba(0,0,0,.2);background:linear-gradient(150deg,#5a3f2c,#1f1814)" role="img" aria-label="Photo of a smiling woman at a dim café table"></div>
  <div class="photo" style="left:196px;top:284px;width:264px;height:273px;border:4px solid #fff;box-shadow:0 1px 5px rgba(0,0,0,.2);background:linear-gradient(170deg,#4a3a30,#a77b4c)" role="img" aria-label="Photo of friends chatting over drinks at a wooden table"></div>
  <h2 class="abs about-title">ABOUT US</h2>
  <div class="abs about-rule"></div>
  <div class="abs about-copy">
    <p>Crewplorvane is dedicated to cultivating a positive culture of leadership for its team members' professional and personal development, and this person-focused mentality transfers throughout the company from partners to our teams to guests. We strive to ensure each team member feels valued in all aspects of their role, reinforcing the importance of fostering a self- sustaining culture of success where everyone makes a team effort to communicate and overcome adversity.</p>
    <p>At Crewplorvane, we are in the business of ensuring that our team members feel happy to come to work each day. We believe in collaboration, innovation, inspiration, and mutual respect. Everyone deserves to work someone wonderful, and at Crewplorvane, we are enthusiastic about creating a supported, robust culture. After all, happy team members mean happy guests, and we love to facilitate positive interactions among guest-facing teams.</p>
  </div>
  <div class="corner-mark">Crewplorvane</div>
</section>

<section class="slide slide-values">
  <div class="abs centered" style="top:52px">
    <h2 class="heading">OUR CORE VALUES</h2>
    <div class="rule"></div>
  </div>
  <svg class="abs" width="1098" height="620" viewBox="0 0 1098 620">
    <defs>
      <radialGradient id="hubShade" cx=".5" cy=".4" r=".6">
        <stop offset="0" stop-color="#ffffff"/>
        <stop offset="1" stop-color="#e2e4e5"/>
      </radialGradient>
    </defs>
    <g>
      <path d="M194 204 Q112 351 202 498 L330 400 Q290 351 330 280 Z" fill="var(--teal)"/>
      <path d="M317 204 Q232 351 358 498 L470 380 Q450 351 470 310 Z" fill="var(--ocean)"/>
    </g>
    <g transform="translate(1054,0) scale(-1,1)">
      <path d="M194 204 Q112 351 202 498 L330 400 Q290 351 330 280 Z" fill="var(--mint)"/>
      <path d="M317 204 Q232 351 358 498 L470 380 Q450 351 470 310 Z" fill="var(--lime)"/>
    </g>
    <circle cx="527" cy="351" r="130" fill="#d7dadb"/>
    <circle cx="527" cy="351" r="124" fill="url(#hubShade)"/>
    <text class="hub-name" x="527" y="359" text-anchor="middle">Crewplorvane</text>
    <g fill="none" stroke="#fff" stroke-width="2.2" stroke-linecap="round" stroke-linejoin="round">
      <path d="M227 325 h26 l8 8 v30 h-34 z M234 338 h14 M234 346 h10 M234 354 h12"/>
      <rect x="253" y="354" width="12" height="10" rx="2"/>
      <circle cx="367" cy="328" r="5"/><circle cx="390" cy="328" r="5"/><circle cx="379" cy="344" r="3.5"/>
      <path d="M360 360 v-18 q7-6 14 0 v18 M383 360 v-18 q7-6 14 0 v18"/>
      <circle cx="703" cy="351" r="22"/><circle cx="703" cy="351" r="13"/><circle cx="703" cy="351" r="4"/>
      <path d="M706 348 l18 -18 M718 330 h6 v6"/>
      <path d="M795 375 l18 -40 l18 40 M813 335 v-14 l10 4 l-10 4 M801 362 l12 -6 l12 6"/>
    </g>
  </svg>
  <div class="value-label" style="left:176px;top:115px"><h3 style="color:var(--teal)">INTEGRITY</h3><p>Integrity in everything we do. Do the right thing, even when no one is looking.</p></div>
  <div class="value-label" style="left:545px;top:132px"><h3 style="color:var(--lime)">RESPECT</h3><p>We care for one another, praise efforts, recognize progress, and reward results.</p></div>
  <div class="value-label" style="left:300px;top:506px"><h3 style="color:var(--ocean)">FAMILY</h3><p>Family first, always. All decisions must benefit our family and the company.</p></div>
  <div class="value-label" style="left:689px;top:511px"><h3 style="color:var(--mint)">PASSION</h3><p>We are positive, hardworking, and disciplined in all we do, which stems from our innate passion.</p></div>
  <div class="corner-mark">Crewplorvane</div>
</section>

<section class="slide slide-team">
  <div class="abs centered" style="top:36px">
    <h2 class="heading">MEET THE TEAM</h2>
    <div class="rule"></div>
  </div>
  <div class="cards">
    <article class="team-card">
      <div class="stars"><span class="quote-mark">“</span>★★★★★</div>
      <blockquote>Growing up Wichita, Kansas, where Birchwood's started, Miles has long felt a connection with the group that started the concept, enjoying the food, culture, and opportunity to be a part of this incredible brand. Miles has owned and operated businesses since the young age of eight, starting as the neighborhood kid who mowed lawns</blockquote>
      <div class="person"><div class="avatar" role="img" aria-label="Portrait of Miles Harrow"></div><h4>MILES HARROW,<br>CEO</h4></div>
    </article>
    <article class="team-card">
      <div class="stars"><span class="quote-mark">“</span>★★★★★</div>
      <blockquote>Nora Kessel is a brilliant veteran of the finance and accounting industries, utilizing her experience to elevate Crewplorvane and its team members and customers. With two years (and counting) under her belt with Crewplorvane, Nora has immediately connected with the family-feeling of this company and enjoys the ongoing learning process of working in a new industry</blockquote>
      <div class="person"><div class="avatar" role="img" aria-label="Portrait of Nora Kessel"></div><h4>NORA KESSEL,<br>CONTROLLER</h4></div>
    </article>
    <article class="team-card">
      <div class="stars"><span class="quote-mark">“</span>★★★★★</div>
      <blockquote>Seizing opportunities to change peoples' lives, in front of and behind the counter, Owen Pratt genuinely enjoys the people-aspect of the food and service industries. At 19 years old, an Area Director had told Owen that he believed Owen was born for this industry and should consider making it his passion</blockquote>
      <div class="person"><div class="avatar" role="img" aria-label="Portrait of Owen Pratt"></div><h4>OWEN PRATT,<br>COO</h4></div>
    </article>
  </div>
  <div class="corner-mark">Crewplorvane</div>
</section>

<section class="slide slide-services">
  <div class="abs centered" style="top:36px">
    <h2 class="heading">WHAT WE DO</h2>
    <div class="rule"></div>
  </div>
  <div class="cards">
    <article class="service">
      <div class="photo" style="background:linear-gradient(170deg,#2a1f18,#6b4a2e 60%,#2d3a2c)" role="img" aria-label="Photo of a warmly lit restaurant dining room"></div>
      <h3 style="background:var(--teal)">RESTAURANTS</h3>
    </article>
    <article class="service">
      <div class="photo" style="background:linear-gradient(150deg,#b9a48c,#d7b48a 50%,#8a6a4a)" role="img" aria-label="Photo of a hand holding house keys over a desk"></div>
      <h3 style="background:var(--ocean)">REAL ESTATE</h3>
    </article>
    <article class="service">
      <div class="photo" style="background:linear-gradient(160deg,#4a5560,#1e2630 60%,#3a4450)" role="img" aria-label="Photo of a developer typing code on a laptop"></div>
      <h3 style="background:var(--forest)">DEVELOPMENT</h3>
    </article>
  </div>
  <div class="corner-mark">Crewplorvane</div>
</section>

<section class="slide slide-thanks">
  <h2 class="abs centered thanks-title">THANK YOU</h2>
</section>

</body>
</html>
```